Australian Sports Podiatry Business needs a Vantor Summerfest marketing flyer

The Stride Hub is looking for a double sided DLflyer to send out to homes which is targeted at people interested in being fit and healthy. To include:

the Vantor Summerfest logo and colours
sporty background

Are you Ready For Rio?
Whatever Your Goals, We'll Keep You On Track
National and International Sports Experience
Lorvane Ablegames (and logo if possible)
Kestrow Unity Crown Games (and logo if poss)
Dunmere Tri-Sport Global Finals (+logo)
Dunmere Galloway Shield Tennis (+logo)

The Stride Hub name, logo, phone number 9271 6028, website www.thestridehub.example, email info@thestridehub.example

Dr Marek Ondravelli's Background:
Marek's has 20 years experience in the field of Sports Medicine and lower limb biomechanics, and he has had extensive experience with treatment of elite athletes from the Calbrook Institute of Athletics, the Fenwell Athletes Lodge, the Calbrook Stormhawks, Tolvane Harriers and the Tolvane Nightjars. He was also selected for the BRELT Medical Team to provide Podiatry Services at the Lorvane 2000 Ablegames, the 2000 GMV Global Tri-Sport Finals, the Kestrow 2006 Unity Crown Games and the Dunmere 2013 Galloway Shield. Marek now treats many athletes from all disciplines in Perth and surrounding areas.

In 1999 Marek became the Director and Senior Podiatrist for The Stride Hub in Perth, Western Australia. Since then he has also been a Director of Athletic Care Federation (ACF), WA Director for the Southern College of Lower-Limb Exercise Care (SCLEC), and an External Advisor to the Halvorne Coastal University’s Podiatric Medicine Unit. He is currently road testing minimalist running shoes for optimised performance and injury prevention.

Marek has always been involved with high level sports, having held a 4x400m Australian Record and also played 1st Division Hockey. He is now training for the Veterans Track Global Finals in October, and volunteers at Quenby Comets Junior Track. He also enjoys keeping fit by running after his 3 kids Brisa, Matilde, and Oskar.

Target Market(s)

People interested in being fit and healthy

Industry/Entity Type

Medical

Requirements
Must have
• To include:
• the Vantor Summerfest logo and colours
• sporty background
• Are you Ready For Rio?
• Whatever Your Goals, We'll Keep You On Track
• National and International Sports Experience
• Lorvane Ablegames (and logo if possible)
• Kestrow Unity Crown Games (and logo if poss)
• Dunmere Tri-Sport Global Finals (+logo)
• Dunmere Galloway Shield Tennis (+logo)
• The Stride Hub name, logo, phone number 9271 6028, website www.thestridehub.example, email info@thestridehub.example
• Dr Marek Ondravelli's Background:
• Marek's has 20 years experience in the field of Sports Medicine and lower limb biomechanics, and he has had extensive experience with treatment of elite athletes from the Calbrook Institute of Athletics, the Fenwell Athletes Lodge, the Calbrook Stormhawks, Tolvane Harriers and the Tolvane Nightjars. He was also selected for the BRELT Medical Team to provide Podiatry Services at the Lorvane 2000 Ablegames, the 2000 GMV Global Tri-Sport Finals, the Kestrow 2006 Unity Crown Games and the Dunmere 2013 Galloway Shield. Marek now treats many athletes from all disciplines in Perth and surrounding areas.
• In 1999 Marek became the Director and Senior Podiatrist for The Stride Hub in Perth, Western Australia. Since then he has also been a Director of Athletic Care Federation (ACF), WA Director for the Southern College of Lower-Limb Exercise Care (SCLEC), and an External Advisor to the Halvorne Coastal University’s Podiatric Medicine Unit. He is currently road testing minimalist running shoes for optimised performance and injury prevention.
Nice to have
• Marek has always been involved with high level sports, having held a 4x400m Australian Record and also played 1st Division Hockey. He is now training for the Veterans Track Global Finals in October, and volunteers at Quenby Comets Junior Track. He also enjoys keeping fit by running after his 3 kids Brisa, Matilde, and Oskar.

```html
<!DOCTYPE html>
<html lang="en">
<head>
<meta charset="utf-8">
<title>The Stride Hub – DL Flyer</title>
<link href="https://fonts.googleapis.com/css2?family=Bebas+Neue&family=Montserrat:wght@400;600;700;800&display=swap" rel="stylesheet">
<style>
  :root{
    --bg:#efe9dc;
    --white:#ffffff;
    --brand-blue:#1f5fae;
    --brand-orange:#ee8a1c;
    --field-green:#4f9a2c;
    --field-green-dark:#2f6a1c;
    --band-dark:#3b1222;
    --magenta:#d6207f;
    --teal:#16a39a;
    --purple:#4b1d6e;
    --purple-deep:#2e1150;
    --ink:#1d2a44;
  }
  *{box-sizing:border-box;margin:0;padding:0}
  html,body{width:1200px;height:1000px;overflow:hidden;background:var(--bg);font-family:'Montserrat',sans-serif}
  .flyer{position:absolute;top:35px;width:440px;height:930px;overflow:hidden;background:var(--white);box-shadow:0 4px 14px rgba(0,0,0,.18)}
  .flyer--front{left:120px}
  .flyer--back{left:640px}

  /* shared brand lockup */
  .brand{position:absolute;display:flex;flex-direction:column;align-items:center}
  .brand__mark{width:64px;height:64px;border-radius:50%;background:var(--brand-blue);border:4px solid var(--brand-orange)}
  .brand__name{margin-top:6px;font-weight:700;font-size:19px;color:var(--brand-blue);letter-spacing:-.2px}
  .brand__url{font-size:9px;font-weight:600;color:var(--ink);letter-spacing:.5px}

  /* front */
  .front__brand{left:0;right:0;top:18px}
  .front__photo{position:absolute;left:0;top:0;width:440px;height:650px;
    background:linear-gradient(160deg,#8fc24a 0%,var(--field-green) 40%,var(--field-green-dark) 100%);
    clip-path:polygon(0 120px,230px 178px,440px 40px,440px 650px,0 650px)}
  .front__accent{position:absolute;left:0;top:0;width:440px;height:650px;background:var(--brand-orange);
    clip-path:polygon(0 120px,130px 153px,0 230px)}
  .headline{position:absolute;left:22px;top:235px;font-family:'Bebas Neue',sans-serif;font-size:72px;line-height:.86;color:var(--white)}
  .event-name{position:absolute;left:24px;top:500px;font-family:'Bebas Neue',sans-serif;font-size:34px;line-height:.95;color:var(--white)}
  .goals-band{position:absolute;left:-20px;top:598px;width:480px;height:100px;background:var(--band-dark);transform:rotate(-3deg)}
  .goals{position:absolute;left:20px;top:608px;font-family:'Bebas Neue',sans-serif;font-size:36px;line-height:.95;color:var(--white);transform:rotate(-3deg);transform-origin:left top}
  .experience{position:absolute;left:0;top:690px;width:440px;height:180px;background:var(--magenta)}
  .experience__title{position:absolute;left:0;right:0;top:14px;text-align:center;color:var(--white);font-size:11px;font-weight:600;letter-spacing:1.4px}
  .events{position:absolute;left:14px;right:14px;top:40px;display:flex;justify-content:space-between}
  .event{width:98px;display:flex;flex-direction:column;align-items:center;text-align:center}
  .event__badge{width:36px;height:36px;border-radius:50%;background:rgba(255,255,255,.85);margin-bottom:6px}
  .event__name{font-size:9px;font-weight:800;line-height:1.15;color:var(--white);text-transform:uppercase}
  .contact{position:absolute;left:0;bottom:0;width:440px;height:60px;display:flex;align-items:center;justify-content:center;gap:34px;color:var(--white);font-size:13px;font-weight:600}
  .contact--front{background:var(--teal)}
  .contact__item{display:flex;align-items:center;gap:7px}

  /* back */
  .back__brand{left:30px;top:40px}
  .portrait{position:absolute;right:0;top:0;width:230px;height:250px;background:linear-gradient(180deg,#f4f4f6 0%,#dfe4ec 100%)}
  .back__shapes{position:absolute;left:0;top:0}
  .doctor{position:absolute;right:30px;top:258px;text-align:right}
  .doctor__name{font-weight:800;font-size:22px;line-height:1.05;color:var(--white);text-transform:uppercase}
  .doctor__role{margin-top:4px;font-weight:700;font-size:17px;color:var(--brand-orange)}
  .bio{position:absolute;left:32px;right:32px;top:400px;color:var(--white);font-size:9.6px;line-height:1.5;text-align:justify}
  .bio p+p{margin-top:10px}
  .back__footer{position:absolute;left:0;bottom:0;width:440px;height:130px;background:linear-gradient(160deg,var(--purple) 0%,var(--purple-deep) 100%)}
  .back__web{position:absolute;right:32px;top:26px;color:var(--white);font-weight:700;font-size:15px;letter-spacing:.5px}
  .back__contact{position:absolute;right:32px;top:56px;display:flex;gap:22px;color:var(--white);font-size:13px;font-weight:600}
</style>
</head>
<body>

<section class="flyer flyer--front" aria-label="Flyer front">
  <div class="front__photo" role="img" aria-label="Green-toned photo of athletes running through a steeplechase water jump"></div>
  <div class="front__accent"></div>
  <div class="brand front__brand">
    <div class="brand__mark"></div>
    <div class="brand__name">The Stride Hub</div>
    <div class="brand__url">www.thestridehub.example</div>
  </div>
  <h1 class="headline">Are<br>You<br>Ready<br>For</h1>
  <div class="event-name">Vantor<br>Summerfest</div>
  <div class="goals-band"></div>
  <p class="goals">Whatever your goals,<br>we'll keep you on track</p>
  <div class="experience">
    <p class="experience__title">NATIONAL AND INTERNATIONAL SPORTS EXPERIENCE</p>
    <div class="events">
      <div class="event"><span class="event__badge"></span><span class="event__name">Lorvane Ablegames</span></div>
      <div class="event"><span class="event__badge"></span><span class="event__name">Kestrow Unity Crown Games</span></div>
      <div class="event"><span class="event__badge"></span><span class="event__name">Dunmere Tri-Sport Global Finals</span></div>
      <div class="event"><span class="event__badge"></span><span class="event__name">Dunmere Galloway Shield Tennis</span></div>
    </div>
  </div>
  <div class="contact contact--front">
    <span class="contact__item">
      <svg width="16" height="16" viewBox="0 0 16 16"><circle cx="8" cy="8" r="7" fill="none" stroke="#fff" stroke-width="1.4"/><path d="M5.5 4.5l1.5 0 .7 2-1 .8a5 5 0 0 0 2 2l.8-1 2 .7v1.5c-3.5.5-6.5-2.5-6-6z" fill="#fff"/></svg>
      9271 6028</span>
    <span class="contact__item">
      <svg width="18" height="13" viewBox="0 0 18 13"><rect x=".7" y=".7" width="16.6" height="11.6" fill="none" stroke="#fff" stroke-width="1.4"/><path d="M1 1l8 6 8-6" fill="none" stroke="#fff" stroke-width="1.4"/></svg>
      info@thestridehub.example</span>
  </div>
</section>

<section class="flyer flyer--back" aria-label="Flyer back">
  <div class="portrait" role="img" aria-label="Photo of Dr Marek Ondravelli in shirt and tie"></div>
  <svg class="back__shapes" width="440" height="930" viewBox="0 0 440 930">
    <polygon points="0,228 440,244 440,930 0,930" fill="var(--brand-blue)"/>
    <polygon points="0,385 440,338 440,930 0,930" fill="var(--brand-orange)"/>
  </svg>
  <div class="brand back__brand">
    <div class="brand__mark"></div>
    <div class="brand__name">The Stride Hub</div>
  </div>
  <div class="doctor">
    <h2 class="doctor__name">Dr. Marek<br>Ondravelli</h2>
    <p class="doctor__role">Podiatrist</p>
  </div>
  <div class="bio">
    <p>Marek's has 20 years experience in the field of Sports Medicine and lower limb biomechanics, and he has had extensive experience with treatment of elite athletes from the Calbrook Institute of Athletics, the Fenwell Athletes Lodge, the Calbrook Stormhawks, Tolvane Harriers and the Tolvane Nightjars. He was also selected for the BRELT Medical Team to provide Podiatry Services at the Lorvane 2000 Ablegames, the 2000 GMV Global Tri-Sport Finals, the Kestrow 2006 Unity Crown Games and the Dunmere 2013 Galloway Shield. Marek now treats many athletes from all disciplines in Perth and surrounding areas.</p>
    <p>In 1999 Marek became the Director and Senior Podiatrist for The Stride Hub in Perth, Western Australia. Since then he has also been a Director of Athletic Care Federation (ACF), WA Director for the Southern College of Lower-Limb Exercise Care (SCLEC), and an External Advisor to the Halvorne Coastal University’s Podiatric Medicine Unit. He is currently road testing minimalist running shoes for optimised performance and injury prevention.</p>
    <p>Marek has always been involved with high level sports, having held a 4x400m Australian Record and also played 1st Division Hockey. He is now training for the Veterans Track Global Finals in October, and volunteers at Quenby Comets Junior Track. He also enjoys keeping fit by running after his 3 kids Brisa, Matilde, and Oskar.</p>
  </div>
  <div class="back__footer">
    <p class="back__web">www.thestridehub.example</p>
    <div class="back__contact">
      <span class="contact__item">
        <svg width="16" height="16" viewBox="0 0 16 16"><circle cx="8" cy="8" r="7" fill="none" stroke="#fff" stroke-width="1.4"/><path d="M5.5 4.5l1.5 0 .7 2-1 .8a5 5 0 0 0 2 2l.8-1 2 .7v1.5c-3.5.5-6.5-2.5-6-6z" fill="#fff"/></svg>
        9271 6028</span>
      <span class="contact__item">
        <svg width="18" height="13" viewBox="0 0 18 13"><rect x=".7" y=".7" width="16.6" height="11.6" fill="none" stroke="#fff" stroke-width="1.4"/><path d="M1 1l8 6 8-6" fill="none" stroke="#fff" stroke-width="1.4"/></svg>
        info@thestridehub.example</span>
    </div>
  </div>
</section>

</body>
</html>
```